Business Card Design for ReaL ESTATE AGENT

New Business Cards for a real estate agent in Jacksonville, FL. My specialty is urban core, historic districts but sell through out the city. Company Name is Quill and Harbor Realty a division of the Vantrell Companies. The card needs to convey an essence of professionalism, knowledge and success.

Target Market(s)

Home buyers and Sellers

Industry/Entity Type

Real Estate

Contact Information for Business Card

Double sided

Font styles to use
Sans Serif

Requirements
Must have
• My logs and photo (provided). My contact information as follows:
• Derek Holloway
• Cell 904-618-3092
• Office 904-731-6248
• Email derekholloway@mailvantor.com
Nice to have
• Tag Line - Exceptional Effort. Proven Results.

```html
<!DOCTYPE html>
<html lang="en">
<head>
<meta charset="utf-8">
<title>Quill and Harbor Realty – Business Card</title>
<link rel="stylesheet" href="https://fonts.googleapis.com/css2?family=Arimo:ital,wght@0,400;0,700;1,700&display=swap">
<style>
  :root {
    --paper: #f3f0ea;
    --ink: #2b2b2b;
    --brand-red: #e8553f;
    --logo-red: #c6432f;
    --frame: #c9432f;
    --frame-dark: #3a2a26;
    --photo-tone-a: #8a8f96;
    --photo-tone-b: #5a4a44;
    --white: #ffffff;
  }
  * { margin: 0; padding: 0; box-sizing: border-box; }
  html, body { width: 720px; height: 1200px; overflow: hidden; background: var(--paper); }
  .card {
    position: relative;
    width: 720px;
    height: 1200px;
    background: var(--paper);
    font-family: "Arimo", Arial, sans-serif;
    color: var(--ink);
    overflow: hidden;
  }
  .portrait {
    position: absolute;
    left: 232px; top: 86px;
    width: 256px; height: 256px;
    border-radius: 50%;
    border: 5px solid var(--frame);
    box-shadow: 0 0 0 4px var(--frame-dark) inset;
    background: radial-gradient(circle at 50% 40%, var(--photo-tone-a), var(--photo-tone-b));
  }
  .brand {
    position: absolute;
    left: 0; top: 392px;
    width: 720px;
    display: flex;
    flex-direction: column;
    align-items: center;
    gap: 20px;
  }
  .brand-mark {
    width: 90px; height: 90px;
    border: 5px solid var(--logo-red);
  }
  .brand-name {
    font-weight: 700;
    font-size: 42px;
    letter-spacing: 2px;
    color: var(--logo-red);
    text-align: center;
    line-height: 1.2;
  }
  .contact {
    position: absolute;
    left: 50%; top: 668px;
    transform: translateX(-50%);
    list-style: none;
    white-space: nowrap;
  }
  .contact li {
    display: flex;
    align-items: center;
    height: 36px;
    font-size: 26px;
    margin-bottom: 6px;
  }
  .contact li.phone-first { margin-top: 8px; }
  .contact svg { width: 26px; height: 26px; margin-right: 18px; flex: none; fill: none; stroke: var(--ink); stroke-width: 2; }
  .contact svg .solid { fill: var(--ink); stroke: none; }
  .footer-band {
    position: absolute;
    left: 0; top: 830px;
    width: 720px; height: 370px;
  }
  .address {
    position: absolute;
    left: 0; top: 912px;
    width: 720px;
    text-align: center;
    color: var(--white);
    font-size: 27px;
    line-height: 38px;
  }
  .address .agent-name { font-weight: 700; }
  .role {
    position: absolute;
    left: 0; top: 1036px;
    width: 720px;
    text-align: center;
    font-weight: 700;
    font-style: italic;
    font-size: 34px;
    color: #1d1d1d;
    letter-spacing: 0.5px;
  }
</style>
</head>
<body>
<main class="card">
  <div class="portrait" role="img" aria-label="Portrait photo of the agent"></div>

  <div class="brand">
    <div class="brand-mark"></div>
    <div class="brand-name">QUILL AND HARBOR<br>REALTY</div>
  </div>

  <ul class="contact">
    <li>
      <svg viewBox="0 0 24 24"><circle cx="12" cy="12" r="10"/><ellipse cx="12" cy="12" rx="4.5" ry="10"/><path d="M2 12h20M4 7h16M4 17h16"/></svg>
      www.quillharborhomes.com
    </li>
    <li>
      <svg viewBox="0 0 24 24"><rect x="2" y="5" width="20" height="14" class="solid"/><path d="M2 5l10 8 10-8" stroke="#f3f0ea"/></svg>
      derekholloway@mailvantor.com
    </li>
    <li class="phone-first">
      <svg viewBox="0 0 24 24"><path class="solid" d="M2 8c0-2 4-4 10-4s10 2 10 4v2h-5V8H7v2H2z"/><rect class="solid" x="5" y="11" width="14" height="9" rx="1"/></svg>
      904 . 618 . 3092
    </li>
    <li>
      <svg viewBox="0 0 24 24"><rect class="solid" x="3" y="9" width="18" height="9" rx="1"/><rect x="7" y="3" width="10" height="6"/><rect x="7" y="15" width="10" height="6" fill="#f3f0ea"/></svg>
      904 . 731 . 6248
    </li>
  </ul>

  <svg class="footer-band" viewBox="0 0 720 370" preserveAspectRatio="none">
    <path fill="var(--brand-red)" d="M0 54 C40 54 70 22 120 22 L600 22 C650 22 680 54 720 54 L720 370 L0 370 Z"/>
  </svg>

  <p class="address"><span class="agent-name">Derek Holloway</span><br>Jacksonville, Florida 32202</p>
  <p class="role">A REAL ESTATE AGENT</p>
</main>
</body>
</html>
```